CPR training postcard

This project is for an oversized postcard that will be mailed from Brivon Health & Safety to local small businesses in the following categories: dentists, podiatrists, optometrists, chiropractors, child care centers, and home health care agencies.
The postcard should mention that we are local, that we offer CPR for Professional Rescuers (BLS), in addition to layperson classes. It should also mention that we teach the classes in their offices or homes at a time convenient for them.
Both attached logos should appear in the design. You can also leverage the images and text from my website: www.brivonlifesaving.example
If any images are selected for the final, I can send the high resolution versions.
The colors should be bold, yet professional. It should capture attention.
Perhaps an eye capturing phrase: Is your CPR certification current? What about your staff?
Specs:
Full Bleed Size
8.64" x 5.59"
219 x 142 mm
2592 x 1677 pixels
Document Trim Size
8.52" x 5.47"
216 x 139 mm
2556 x 1642 pixels
Please include our phone number and web address in designs, as well as our Facebook page
All can be found on our website.
All designs must have the Brivon Health and Safety logo on the front to be considered. All designs must show both sides of the post card. Single side designs will not be considered.
The recipients have been trained in the past- they know what to do. Most are required to be re certified every year or two. Thus, a message asking if their certification is current is more relevant than asking whether they know what to do.
Target Market(s)
Medical and child care professionals. Design should focus on medical professionals.
Industry/Entity Type
Home Health Care
Requirements
Must have
- Bold text drawing in recipient. Brivon logo on front. Front and back designs must be shown. Full color front and back. Website, telephone number, Facebook page.
Nice to have
- Should focus on CPR and not first aid in the images

```html
<!DOCTYPE html>
<html lang="en">
<head>
<meta charset="utf-8">
<title>Brivon Health &amp; Safety – Back Postcard</title>
<link href="https://fonts.googleapis.com/css2?family=Fira+Sans+Condensed:ital,wght@0,500;0,700;0,800;1,700&family=Open+Sans:wght@400&display=swap" rel="stylesheet">
<style>
  :root {
    --stage: #9c9d9f;
    --brand-red: #d2001c;
    --brand-red-deep: #a60d22;
    --paper: #ffffff;
    --paper-shade: #d7d8da;
    --stamp-line: #cfd0d2;
    --ink-white: #ffffff;
    --ink-grey: #5a5b5d;
  }
  * { margin: 0; padding: 0; box-sizing: border-box; }
  html, body {
    width: 1200px; height: 1000px; overflow: hidden;
    background: var(--stage);
  }
  .stage { position: relative; width: 1200px; height: 1000px; }
  .postcard {
    position: absolute; left: 45px; top: 74px;
    width: 1108px; height: 718px;
    box-shadow: 6px 8px 10px rgba(0,0,0,0.45);
  }
  .postcard-art { position: absolute; inset: 0; display: block; }
  .brand-plate {
    position: absolute; left: 28px; top: 30px;
    width: 330px; height: 113px;
    background: var(--paper); border-radius: 16px;
    display: flex; align-items: center; justify-content: center; gap: 12px;
  }
  .brand-dot {
    flex: 0 0 30px; width: 30px; height: 30px; border-radius: 50%;
    background: var(--brand-red);
  }
  .brand-name {
    font-family: "Fira Sans Condensed", sans-serif;
    font-weight: 700; font-size: 27px; white-space: nowrap;
    color: var(--brand-red); line-height: 1;
  }
  .brand-address {
    position: absolute; left: 38px; top: 156px;
    font-family: "Fira Sans Condensed", sans-serif;
    font-weight: 500; font-size: 15px; letter-spacing: 0.6px;
    color: var(--ink-white);
  }
  .headline {
    position: absolute; left: 375px; top: 48px;
    font-family: "Fira Sans Condensed", sans-serif;
    color: var(--ink-white); text-transform: uppercase;
  }
  .headline-main { display: block; font-weight: 800; font-size: 39px; letter-spacing: 1.2px; line-height: 42px; }
  .headline-sub { display: block; font-weight: 500; font-size: 31px; letter-spacing: 1.3px; line-height: 40px; }
  .tagline {
    position: absolute; left: 33px; top: 200px;
    font-family: "Fira Sans Condensed", sans-serif;
    font-style: italic; font-weight: 700; font-size: 20.5px;
    line-height: 25px; color: var(--ink-white);
  }
  .offer {
    position: absolute; left: 300px; top: 232px; width: 580px;
    font-family: "Fira Sans Condensed", sans-serif;
  }
  .offer-question {
    font-weight: 800; font-size: 25px; line-height: 30px;
    color: var(--brand-red);
  }
  .offer-detail {
    margin-top: 8px; font-weight: 500; font-size: 17px; line-height: 22px;
    color: var(--ink-grey);
  }
  .offer-contact {
    margin-top: 10px; font-weight: 700; font-size: 16px; line-height: 21px;
    color: var(--brand-red-deep);
  }
  .view-label {
    position: absolute; left: 0; width: 1200px; top: 868px;
    text-align: center;
    font-family: "Open Sans", sans-serif; font-weight: 400;
    font-size: 40px; letter-spacing: 3px; color: var(--ink-white);
    text-shadow: 2px 3px 4px rgba(0,0,0,0.35);
  }
</style>
</head>
<body>
<main class="stage">
  <section class="postcard" aria-label="Postcard back">
    <svg class="postcard-art" width="1108" height="718" viewBox="0 0 1108 718" aria-hidden="true">
      <defs>
        <radialGradient id="red-field" cx="0.15" cy="0.35" r="0.9">
          <stop offset="0" stop-color="#d2001c"/>
          <stop offset="1" stop-color="#a60d22"/>
        </radialGradient>
        <linearGradient id="paper-field" x1="0.15" y1="0.15" x2="0.55" y2="0.75">
          <stop offset="0" stop-color="#d7d8da"/>
          <stop offset="1" stop-color="#ffffff"/>
        </linearGradient>
        <filter id="edge-shadow" x="-10%" y="-10%" width="120%" height="120%">
          <feDropShadow dx="-4" dy="3" stdDeviation="4" flood-color="#000" flood-opacity="0.35"/>
        </filter>
      </defs>
      <rect class="red-field" width="1108" height="718" fill="url(#red-field)"/>
      <path class="address-field" filter="url(#edge-shadow)" fill="url(#paper-field)"
        d="M165 718 C120 620 100 480 140 370 C190 240 360 155 600 148 C760 144 860 160 911 176 L911 0 L1108 0 L1108 718 Z"/>
      <rect class="stamp-box" x="930" y="22" width="153" height="152" fill="none" stroke="#cfd0d2" stroke-width="1.5"/>
    </svg>

    <div class="brand-plate">
      <span class="brand-dot"></span>
      <span class="brand-name">Brivon Health &amp; Safety</span>
    </div>
    <p class="brand-address">48 Larkmoor Rd, Fenwick, NY 10472</p>

    <h1 class="headline">
      <span class="headline-main">CPR Training Classes</span>
      <span class="headline-sub">Offer Service in the Local Area</span>
    </h1>

    <p class="tagline">We look forward<br>to demonstrating why<br>you need not look<br>anywhere else.</p>

    <div class="offer">
      <p class="offer-question">Is your CPR certification current? What about your staff?</p>
      <p class="offer-detail">Local CPR for Professional Rescuers (BLS) plus layperson classes, taught in your office or home at a time convenient for you.</p>
      <p class="offer-contact">(914) 555-0182 &nbsp;·&nbsp; www.brivonlifesaving.example<br>facebook.com/BrivonHealthSafety</p>
    </div>
  </section>
  <p class="view-label">BACK POSTCARD</p>
</main>
</body>
</html>
```